Door Hanger Design for Electricians Serving Homes

I would like our logo incorporated into the door hanger. We would like a place for a tear off section on the bottom of the hanger with our contact information: K&T Electric - (555) 318-4702 - www.kandtelectric.example - info@kandtelectric.example.
Door Hanger Script
Front Side of the Door Hanger:
[Company Logo]
Need a Reliable Electrician?
Your Local Electrical Expert is Just Around the Corner!
• Quick Response Times
• Affordable Rates
• Quality Workmanship
• Fully Licensed & Insured
• Special Offer:
• 10% OFF Your First Service Call!
Back Side of the Door Hanger:
Don't Let Electrical Issues Keep You in the Dark!
From flickering lights to complete system upgrades, we've got all your
residential electrical needs covered. Our services include:
• Electrical Repairs & Troubleshooting
• Lighting Installation & Upgrades
• Safety Inspections & Code Compliance
• Energy-Efficient Solutions
• 24/7 Emergency Services
• Why Choose Us?
• Friendly, Local Service
• Over 30 Years of Experience
• Satisfaction Guaranteed
• Upfront Pricing
Call Us Today: [Your Phone Number]
Visit Our Website: [Your Website]
Book Your Appointment Now and Claim Your 10% Discount!
Offer valid for new customers on the first visit only. Mention this door hanger when
booking.
[Your Company Name and Contact Information]
Follow Us on Social Media for More Tips and Special Offers!
[Icons for social media platforms: Chatterpage, Pixmosaic, Quibbler, etc.]
Design Tips:
Use bold, clear fonts for easy reading.
Incorporate your brand colors and logo for instant recognition.
Include a clear call to action (CTA) on both sides.
Add a tear-off section at the bottom with your contact information for
convenience.
Use high-quality images or graphics related to electrical work to catch
the eye.
This door hanger design and copy aim to attract residential clients by
highlighting the benefits of your electrical services, special offers, and
how they can easily get in touch with you for their electrical needs.
The door knocker template will have three of the same design on front and three of the same design on the back. This template is from the print shop.

```html
<!DOCTYPE html>
<html lang="en">
<head>
<meta charset="utf-8">
<title>K&amp;T Electric Door Hanger</title>
<link rel="stylesheet" href="https://fonts.googleapis.com/css2?family=Archivo:wght@400;600;700;800;900&display=swap">
<style>
:root{
  --red:#e8222e;
  --salmon:#ec7a63;
  --black:#111111;
  --white:#ffffff;
  --grey:#9a9ea3;
  --canvas:#f2f2f2;
}
*{box-sizing:border-box;margin:0;padding:0}
html,body{width:1200px;height:1043px;overflow:hidden;background:var(--canvas)}
body{position:relative;font-family:"Archivo",Arial,sans-serif;color:var(--black)}
.hanger-wrap{position:absolute;top:48px;width:186px;height:430px;transform:scale(2.2);transform-origin:top left}
.hanger-wrap.front{left:131px}
.hanger-wrap.back{left:660px}
.hanger{position:relative;width:186px;height:430px;background:var(--white);overflow:hidden;box-shadow:0 1px 3px rgba(0,0,0,.25)}
.abs{position:absolute}
.photo{left:0;top:0;width:186px;height:135px;background:linear-gradient(180deg,#b9bcc0 0%,#d6d8da 55%,rgba(255,255,255,.95) 100%)}
.back .photo{height:120px;background:linear-gradient(180deg,#c3c6c9 0%,#dcdedf 60%,#f4f4f4 100%)}
.top-strip{left:0;top:0;width:128px;height:8px;background:var(--red)}
.logo-box{background:var(--white);display:flex;align-items:center;justify-content:center;text-align:center;font-weight:800;font-size:8px;line-height:1.05;color:var(--black)}
.front .logo-box{left:128px;top:4px;width:54px;height:54px}
.back .logo-box{left:2px;top:2px;width:56px;height:56px}
.hole{width:48px;height:48px;border-radius:50%;background:var(--white);border:1px solid #8c8c8c}
.front .hole{left:23px;top:31px}
.back .hole{left:66px;top:31px}
.slit{height:1px;background:#8c8c8c;transform-origin:left center}
.headline{left:9px;font-weight:900;line-height:1;letter-spacing:-.2px}
.headline .red{color:var(--red)}
.salmon-band{left:0;width:186px;background:var(--salmon);color:var(--white);font-weight:700;padding:0 9px;display:flex;align-items:center}
.pill{width:80px;height:30px;border-radius:15px;background:var(--red);border:1.5px solid #c9c9c9;color:var(--white);font-weight:700;font-size:7px;line-height:1.1;display:flex;align-items:center;gap:5px;padding-left:5px}
.pill svg{flex:none}
.section-title{font-weight:900}
.black-band{left:0;width:186px;background:var(--black);color:var(--white);font-weight:800;text-align:center;display:flex;align-items:center;justify-content:center}
.dash{left:0;width:186px;border-top:1px dashed var(--black)}
.brand-name{left:0;width:186px;text-align:center;font-weight:900;color:var(--black)}
.call-band{left:0;width:186px;height:20px;background:var(--red);color:var(--white);font-weight:800;font-size:10.5px;display:flex;align-items:center;justify-content:center}
.contact-line{left:36px;display:flex;align-items:center;gap:5px;font-size:7.5px;font-weight:700}
.list{list-style:none;left:10px}
.list li{display:flex;align-items:center;gap:5px;height:9.8px}
.list li::before{content:"";width:4px;height:4px;background:var(--black);flex:none}
.list.red li{color:var(--red)}
.list.red li::before{background:var(--red)}
.rule{left:9px;width:177px;height:1px;background:var(--black)}
.rule.red{background:var(--red)}
.social{left:73px;top:389px;display:flex;gap:4px}
.social span{width:10px;height:10px;border-radius:2px;background:var(--red)}
</style>
</head>
<body>

<!-- Front side -->
<div class="hanger-wrap front">
  <section class="hanger">
    <div class="abs photo" role="img" aria-label="Photo of an electrician working on a breaker panel"></div>
    <div class="abs top-strip"></div>
    <div class="abs logo-box">K&amp;T<br>Electric</div>
    <div class="abs hole"></div>
    <div class="abs slit" style="left:42px;top:8px;width:38px;transform:rotate(35deg)"></div>

    <h1 class="abs headline" style="top:89px;font-size:17.5px">NEED A RELIABLE<br><span class="red">ELECTRICIAN?</span></h1>
    <p class="abs salmon-band" style="top:127px;height:23px;font-size:7.6px;line-height:1.05">Your Local Electrical Expert is Just Around the Corner!</p>

    <div class="abs pill" style="left:9px;top:222px;top:222px;top:222px;top:222px;top:222px;display:none"></div>
    <div class="abs pill" style="left:9px;top:222px;display:none"></div>

    <div class="abs pill" style="left:9px;top:222px;display:none"></div>

    <div class="abs pill" style="left:9px;top:222px;display:none"></div>

    <div class="abs pill" style="left:9px;top:222px;display:none"></div>

    <div class="abs pill" style="left:9px;top:222px;display:none"></div>

    <div class="abs pill" style="left:9px;top:222px;display:none"></div>

    <div class="abs pill" style="left:9px;top:222px;display:none"></div>

    <div class="abs pill" style="left:9px;top:177px">
      <svg width="16" height="16" viewBox="0 0 16 16"><circle cx="8" cy="8" r="8" fill="#fff"/><circle cx="9" cy="8.5" r="4" fill="none" stroke="#e8222e" stroke-width="1.4"/><path d="M9 6.5v2.2l1.4 1" stroke="#e8222e" stroke-width="1.2" fill="none"/><path d="M2.5 6.5h2.5M2 8.5h2.5M2.5 10.5h2" stroke="#e8222e" stroke-width="1"/></svg>
      <span>Quick<br>Response</span>
    </div>
    <div class="abs pill" style="left:95px;top:177px">
      <svg width="16" height="16" viewBox="0 0 16 16"><circle cx="8" cy="8" r="8" fill="#fff"/><text x="8" y="11.5" text-anchor="middle" font-family="Archivo,Arial,sans-serif" font-weight="900" font-size="10" fill="#e8222e">$</text></svg>
      <span>Affordable<br>Rates</span>
    </div>
    <div class="abs pill" style="left:9px;top:216px">
      <svg width="16" height="16" viewBox="0 0 16 16"><circle cx="8" cy="8" r="8" fill="#fff"/><path d="M8 3.6l1.3 2.8 3 .3-2.3 2 .7 3-2.7-1.6-2.7 1.6.7-3-2.3-2 3-.3z" fill="#e8222e"/></svg>
      <span>Quality<br>Workmanship</span>
    </div>
    <div class="abs pill" style="left:95px;top:216px">
      <svg width="16" height="16" viewBox="0 0 16 16"><circle cx="8" cy="8" r="8" fill="#fff"/><path d="M4.6 8.2l2.3 2.3 4.5-4.7" stroke="#e8222e" stroke-width="1.8" fill="none"/></svg>
      <span>Fully Licensed<br>&amp; Insured</span>
    </div>

    <h2 class="abs section-title" style="left:0;width:186px;text-align:center;top:257px;font-size:14.5px">SPECIAL OFFER</h2>
    <p class="abs black-band" style="top:276px;height:21px;font-size:10px">10% OFF Your First Service Call!</p>

    <div class="abs dash" style="top:308px"></div>
    <p class="abs brand-name" style="top:321px;font-size:12px">K&amp;T Electric</p>

    <p class="abs call-band" style="top:356px">Call Us Today: (555) 318-4702</p>

    <p class="abs contact-line" style="top:383px">
      <svg width="12" height="12" viewBox="0 0 12 12"><circle cx="6" cy="6" r="6" fill="#111"/><circle cx="6" cy="6" r="3.6" fill="none" stroke="#fff" stroke-width=".8"/><path d="M2.4 6h7.2M6 2.4c-1.6 2-1.6 5.2 0 7.2M6 2.4c1.6 2 1.6 5.2 0 7.2" stroke="#fff" stroke-width=".7" fill="none"/></svg>
      www.kandtelectric.example
    </p>
    <p class="abs contact-line" style="top:401px">
      <svg width="12" height="12" viewBox="0 0 12 12"><circle cx="6" cy="6" r="6" fill="#111"/><rect x="3" y="4" width="6" height="4.2" fill="none" stroke="#fff" stroke-width=".8"/><path d="M3 4l3 2.4L9 4" stroke="#fff" stroke-width=".8" fill="none"/></svg>
      info@kandtelectric.example
    </p>
  </section>
</div>

<!-- Back side -->
<div class="hanger-wrap back">
  <section class="hanger">
    <div class="abs photo" role="img" aria-label="Photo of an electrician inspecting a service panel"></div>
    <div class="abs logo-box">K&amp;T<br>Electric</div>
    <div class="abs hole"></div>
    <div class="abs slit" style="left:92px;top:8px;width:36px;transform:rotate(42deg)"></div>

    <h1 class="abs headline" style="top:85px;font-size:10.2px;left:10px">Don't Let <span class="red">Electrical Issues</span> Keep<br>You in the Dark!</h1>
    <p class="abs salmon-band" style="top:107px;height:19px;font-size:5.2px;line-height:1.2">From flickering lights to complete system upgrades, we've got all your residential electrical needs covered</p>

    <h2 class="abs section-title" style="left:10px;top:131px;font-size:11px">Our Services</h2>
    <div class="abs rule" style="top:145px"></div>
    <ul class="abs list" style="top:148px;font-size:6.3px">
      <li>Electrical Repairs &amp; Troubleshooting</li>
      <li>Lighting Installation &amp; Upgrades</li>
      <li>Safety Inspections &amp; Code Compliance</li>
      <li>Energy-Efficient Solutions</li>
      <li>24/7 Emergency Services</li>
    </ul>

    <h2 class="abs section-title" style="left:10px;top:201px;font-size:11px;color:var(--red)">Why Choose Us?</h2>
    <div class="abs rule red" style="top:215px"></div>
    <ul class="abs list red" style="top:218px;font-size:6.2px">
      <li>Friendly, Local Service</li>
      <li>Over 30 Years of Experience</li>
      <li>Satisfaction Guaranteed</li>
      <li>Upfront Pricing</li>
    </ul>

    <p class="abs black-band" style="top:263px;height:21px;font-size:6.6px;line-height:1.15">Book Your Appointment Now and<br>Claim Your 10% Discount!</p>
    <p class="abs" style="left:0;width:186px;top:287px;text-align:center;font-size:5.4px;font-weight:700;line-height:1.25">Offer valid for new customers on the first visit only.<br>Mention this door hanger when booking.</p>

    <div class="abs dash" style="top:308px"></div>
    <p class="abs brand-name" style="top:320px;font-size:14px">K&amp;T Electric</p>

    <p class="abs call-band" style="top:345px">Call Us Today: (555) 318-4702</p>
    <p class="abs" style="left:0;width:186px;top:370px;text-align:center;font-size:7px;font-weight:800;line-height:1.15">Follow Us on Social Media for More<br>Tips and Special Offers!</p>
    <div class="abs social" aria-label="Chatterpage, Pixmosaic and Quibbler">
      <span></span><span></span><span></span>
    </div>
    <p class="abs" style="left:0;width:186px;top:409px;text-align:center;font-size:7px;font-weight:700">www.kandtelectric.example</p>
  </section>
</div>

</body>
</html>
```